I needed some business cards done for my band. We are a 9 piece funk/horn band that plays a lot of private parties, wedding receptions and music festivals. We'd like a design with vivid colors that incorporates our logo. You can check out our website at www.brasslanternband.example to see what type of vibe we are going for.

```html
<!DOCTYPE html>
<html lang="en">
<head>
<meta charset="utf-8">
<title>Brass Lantern – Business Cards</title>
<link rel="stylesheet" href="https://fonts.googleapis.com/css2?family=Raleway:wght@400;500;700;800&display=swap">
<style>
  :root {
    --stage: #3b3b3d;
    --card: #121212;
    --card-edge: #1c1c1c;
    --lime: #c6e03a;
    --white: #f2f2f2;
    --divider: #4a4a4a;
    --logo-core: #0a0a0a;
  }
  * { margin: 0; padding: 0; box-sizing: border-box; }
  html, body { width: 1200px; height: 1200px; overflow: hidden; }
  body {
    background: var(--stage);
    font-family: "Raleway", Arial, sans-serif;
    display: flex;
    flex-direction: column;
    align-items: center;
    justify-content: center;
    gap: 44px;
  }
  .card {
    position: relative;
    width: 900px;
    height: 514px;
    background: radial-gradient(ellipse at 50% 40%, var(--card-edge), var(--card) 70%);
    border-radius: 34px;
    box-shadow: 0 3px 0 var(--lime), 0 14px 30px rgba(0,0,0,.45);
    overflow: hidden;
  }
  /* front */
  .band-name {
    position: absolute;
    left: 190px;
    top: 78px;
    font-size: 84px;
    font-weight: 800;
    color: var(--lime);
    letter-spacing: -1px;
    line-height: 1;
  }
  .divider {
    position: absolute;
    left: 430px;
    top: 300px;
    width: 1px;
    height: 130px;
    background: var(--divider);
  }
  .member {
    position: absolute;
    left: 120px;
    bottom: 66px;
  }
  .member-name {
    font-size: 36px;
    font-weight: 700;
    color: var(--lime);
    line-height: 1;
  }
  .member-role {
    font-size: 20px;
    font-weight: 500;
    color: var(--white);
    letter-spacing: 1px;
    margin-top: 6px;
  }
  .social {
    display: flex;
    align-items: center;
    gap: 10px;
    margin-top: 14px;
    font-size: 19px;
    color: var(--white);
  }
  .social-dot {
    width: 22px; height: 22px;
    border-radius: 50%;
    background: var(--lime);
  }
  .contact {
    position: absolute;
    left: 462px;
    right: 60px;
    top: 250px;
    list-style: none;
  }
  .contact li {
    display: flex;
    align-items: center;
    gap: 14px;
    font-size: 21px;
    color: var(--white);
    margin-bottom: 14px;
    white-space: nowrap;
  }
  .contact svg { width: 24px; height: 24px; flex: none; }
  /* back */
  .emblem {
    position: absolute;
    left: 50%;
    top: 50%;
    width: 340px;
    height: 340px;
    transform: translate(-50%, -50%);
    border-radius: 50%;
    background: var(--logo-core);
    border: 34px solid var(--lime);
    display: flex;
    align-items: center;
    justify-content: center;
  }
  .emblem-name {
    font-size: 40px;
    font-weight: 800;
    color: var(--lime);
    text-align: center;
    line-height: 1.05;
  }
</style>
</head>
<body>

<section class="card card-front">
  <h1 class="band-name">Brass Lantern</h1>
  <div class="divider"></div>

  <div class="member">
    <div class="member-name">FULL NAME</div>
    <div class="member-role">POSITION</div>
    <div class="social"><span class="social-dot"></span>@brasslanternband</div>
  </div>

  <ul class="contact">
    <li>
      <svg viewBox="0 0 24 24" aria-hidden="true"><path fill="#c6e03a" d="M6.6 10.8a15 15 0 0 0 6.6 6.6l2.2-2.2a1 1 0 0 1 1-.25 11.4 11.4 0 0 0 3.6.57 1 1 0 0 1 1 1V20a1 1 0 0 1-1 1A17 17 0 0 1 3 4a1 1 0 0 1 1-1h3.5a1 1 0 0 1 1 1c0 1.25.2 2.45.57 3.57a1 1 0 0 1-.25 1z"/></svg>
      555.014.2270
    </li>
    <li>
      <svg viewBox="0 0 24 24" aria-hidden="true"><rect x="2" y="5" width="20" height="14" fill="#c6e03a"/><path d="M2 5l10 8 10-8" fill="none" stroke="#121212" stroke-width="1.8"/></svg>
      info@brasslanternband.example
    </li>
    <li>
      <svg viewBox="0 0 24 24" aria-hidden="true"><g fill="none" stroke="#c6e03a" stroke-width="1.8"><circle cx="12" cy="12" r="10"/><ellipse cx="12" cy="12" rx="4.5" ry="10"/><path d="M2 12h20M4 7h16M4 17h16"/></g></svg>
      www.brasslanternband.example
    </li>
  </ul>
</section>

<section class="card card-back">
  <div class="emblem">
    <div class="emblem-name">Brass<br>Lantern</div>
  </div>
</section>

</body>
</html>
```